Velmora and Co Business Card Design

Looking for a business card design. Wanting Smart, Clean and Sharp looking to promote Velmora and Co, our Import Export Business - like Black, White and natural textures. I have uploaded our logo. I like a rounded font but open to other ideas
Being that we have a wide range of products on offer we are looking for a neutral yet eye catching card. We would also like to have Import - Export on the business card to be clear on want our business does.

Target Market(s)

Import export market

Industry/Entity Type

Importer

Contact Information for Business Card

Mr Tobias Kernwell
tobias.kernwell@velmoraandco.com.au
+61 (0) 417 630 284
www.velmoraandco.com.au

Font styles to use
Other font styles liked:
• Unsure of actual font name but something rounded and clean

Colors

Designer to choose colors to be used in the design.

Requirements
Must have
• Instagram icon
• Facebook icon

```html
<!DOCTYPE html>
<html lang="en">
<head>
<meta charset="utf-8">
<title>Velmora and Co – Business Card</title>
<link href="https://fonts.googleapis.com/css2?family=Exo+2:wght@400;500;600&family=Oswald:wght@600&display=swap" rel="stylesheet">
<style>
  :root {
    --ink: #231f20;
    --ink-strip: #1f1c1d;
    --ghost: #333031;
    --paper: #ffffff;
    --text-light: #ffffff;
  }
  * { margin: 0; padding: 0; box-sizing: border-box; }
  html, body { width: 1017px; height: 1200px; overflow: hidden; background: var(--paper); }
  .canvas { position: relative; width: 1017px; height: 1200px; font-family: "Exo 2", sans-serif; }

  /* Front */
  .card-front { position: absolute; left: 0; top: 0; width: 1017px; height: 570px; background: var(--paper); }
  .front-strip { position: absolute; left: 5px; top: 566px; width: 1007px; height: 14px; background: var(--ink-strip); border-radius: 0 0 14px 14px; }
  .brand-lockup { position: absolute; left: 0; right: 0; top: 255px; display: flex; justify-content: center; align-items: center; gap: 22px; }
  .brand-square { width: 44px; height: 44px; border: 7px solid var(--ink); }
  .brand-name { font-family: "Oswald", sans-serif; font-weight: 600; font-size: 52px; letter-spacing: 1px; color: var(--ink); text-transform: uppercase; line-height: 1; }

  /* Back */
  .card-back { position: absolute; left: 0; top: 619px; width: 1016px; height: 580px; background: var(--ink); border-radius: 22px; overflow: hidden; color: var(--text-light); }
  .ghost-name { position: absolute; left: 100px; top: -20px; font-family: "Oswald", sans-serif; font-weight: 600; font-size: 300px; line-height: 0.95; color: var(--ghost); text-transform: uppercase; letter-spacing: 4px; white-space: nowrap; }
  .ghost-name span { display: block; }

  .holder { position: absolute; left: 70px; top: 214px; }
  .holder-name { font-size: 40px; font-weight: 500; line-height: 1.05; }
  .holder-role { font-size: 23px; font-weight: 400; margin-top: 2px; }
  .social { display: flex; align-items: center; gap: 6px; margin-top: 6px; font-size: 24px; font-weight: 500; }
  .social-dot { width: 26px; height: 26px; border-radius: 50%; background: var(--text-light); }
  .social-handle { margin-left: 14px; }

  .contacts { position: absolute; left: 496px; top: 208px; list-style: none; }
  .contacts li { display: flex; align-items: center; gap: 22px; height: 43px; font-size: 24px; font-weight: 500; }
  .contacts svg { width: 28px; height: 28px; flex: none; }

  .trade-line { position: absolute; left: 0; right: 0; top: 520px; display: flex; align-items: center; gap: 14px; }
  .trade-line::before, .trade-line::after { content: ""; flex: 1; height: 2px; background: var(--text-light); }
  .trade-label { font-size: 41px; font-weight: 400; line-height: 1; }
</style>
</head>
<body>
<div class="canvas">
  <section class="card-front">
    <div class="brand-lockup">
      <div class="brand-square"></div>
      <div class="brand-name">Velmora and Co</div>
    </div>
  </section>
  <div class="front-strip"></div>

  <section class="card-back">
    <div class="ghost-name" aria-hidden="true"><span>Velmora</span><span>and Co</span></div>

    <div class="holder">
      <div class="holder-name">Mr. Tobias Kernwell</div>
      <div class="holder-role">Founder &amp; CEO</div>
      <div class="social">
        <span class="social-dot"></span>
        <span class="social-dot"></span>
        <span class="social-handle">@tobias.kernwell</span>
      </div>
    </div>

    <ul class="contacts">
      <li>
        <svg viewBox="0 0 28 28"><circle cx="14" cy="14" r="13" fill="#fff"/><path d="M9.5 7.5l3 .3 1 3.2-1.8 1.4c.9 1.9 2.2 3.2 4 4l1.4-1.8 3.2 1 .3 3-1.6 1.6C14 20 8.5 14.6 8 9.2z" fill="#231f20"/></svg>
        <span>+61 (0) 417 630 284</span>
      </li>
      <li>
        <svg viewBox="0 0 28 28"><circle cx="14" cy="14" r="13" fill="#fff"/><rect x="7.5" y="9.5" width="13" height="9" rx="1" fill="none" stroke="#231f20" stroke-width="1.6"/><path d="M8 10.5l6 4.5 6-4.5" fill="none" stroke="#231f20" stroke-width="1.6"/></svg>
        <span>tobias.kernwell@velmoraandco.com.au</span>
      </li>
      <li>
        <svg viewBox="0 0 28 28"><circle cx="14" cy="14" r="13" fill="#fff"/><circle cx="14" cy="14" r="7.5" fill="none" stroke="#231f20" stroke-width="1.6"/><path d="M6.5 14h15M14 6.5c-3 3.5-3 11.5 0 15M14 6.5c3 3.5 3 11.5 0 15" fill="none" stroke="#231f20" stroke-width="1.3"/></svg>
        <span>www.velmoraandco.com.au</span>
      </li>
    </ul>

    <div class="trade-line"><span class="trade-label">Import-Export</span></div>
  </section>
</div>
</body>
</html>
```